Business card for Luxury Portable Restroom Trailer company

We are a Luxury Portable Restroom Trailer Company Called FALVEX HIRINGS. Based in Orange County California. We provide portable restroom trailers for events, such as, Weddings, Concerts, Charity events, Sporting events, Tournaments, Corporate events, ect. We rent and Sell the Luxury restrooms. Our colors are white, grey, and Orange. As you will see in the logo we uploaded.
There are 2 people in the company so the names and titles will change for the 3 people but card will remain the same. Here is the information for each Person: Desmond Purt CFO 555 018-3374
next Person: Milo Fenwright VP 555 018-3374
Next Person: Owen Fenwright CEO 555 018-3374
Information to include on the card: Luxury Restroom Trailers Rental and Sales. Weddings, Concerts, Charity, Sporting and Corp. Events.

```html
<!DOCTYPE html>
<html lang="en">
<head>
<meta charset="utf-8">
<title>FALVEX HIRINGS – Business Card</title>
<link href="https://fonts.googleapis.com/css2?family=Source+Sans+3:wght@400;600;700&display=swap" rel="stylesheet">
<style>
  :root {
    --bg: #97989a;
    --paper: #ffffff;
    --orange: #f26a21;
    --ink: #4a4a4c;
    --slate: #58585a;
    --slate-deep: #444446;
  }
  * { margin: 0; padding: 0; box-sizing: border-box; }
  html, body { width: 1200px; height: 1200px; overflow: hidden; }
  body {
    background: var(--bg);
    font-family: "Source Sans 3", sans-serif;
    position: relative;
  }
  .card {
    position: absolute;
    left: 231px;
    width: 736px;
    height: 451px;
    overflow: hidden;
  }
  .card--front { top: 116px; background: var(--paper); }
  .card--back { top: 631px; background: var(--slate); }

  .brand-name {
    position: absolute;
    font-weight: 700;
    letter-spacing: 1px;
    white-space: nowrap;
    line-height: 1;
  }
  .card--front .brand-name {
    left: 36px; top: 66px;
    font-size: 50px;
    color: var(--orange);
  }

  .name-marker {
    position: absolute;
    left: 0; top: 248px;
    width: 26px; height: 61px;
    background: var(--orange);
  }
  .person-name {
    position: absolute;
    left: 36px; top: 243px;
    font-size: 38px;
    font-weight: 700;
    color: var(--orange);
    line-height: 1.2;
  }
  .contact {
    position: absolute;
    left: 36px; top: 287px;
    font-size: 25px;
    color: var(--ink);
    line-height: 1.2;
  }
  .contact .label { color: var(--orange); }
  .divider {
    position: absolute;
    left: 36px; top: 330px;
    width: 653px; height: 2px;
    background: var(--orange);
  }
  .tagline {
    position: absolute;
    left: 36px; top: 346px;
    width: 660px;
    font-size: 22.5px;
    line-height: 29px;
    color: var(--ink);
  }

  .emblem-art {
    position: absolute;
    left: 0; top: 0;
    width: 480px; height: 451px;
    background: radial-gradient(ellipse at 35% 55%, var(--slate-deep) 0%, rgba(68,68,70,0.6) 45%, rgba(88,88,90,0) 75%);
  }
  .card--back .brand-name {
    right: 33px; top: 350px;
    font-size: 44px;
    color: var(--paper);
  }
</style>
</head>
<body>
  <section class="card card--front">
    <div class="brand-name">FALVEX HIRINGS</div>
    <div class="name-marker"></div>
    <h1 class="person-name">MILO FENWRIGHT VP</h1>
    <p class="contact"><span class="label">CONTACT:</span> 555 018-3374</p>
    <div class="divider"></div>
    <p class="tagline">Luxury Restroom Trailers Rental and Sales. Weddings, Concerts, Charity, Sporting and Corp. Events.</p>
  </section>

  <section class="card card--back">
    <div class="emblem-art" role="img" aria-label="Large embossed brand emblem in tone-on-tone dark grey"></div>
    <div class="brand-name">FALVEX HIRINGS</div>
  </section>
</body>
</html>
```